Startup Drone Platform Company business card

We are needing a business card design for our employees. We are a startup drone platform. We are looking for a business card that has our logo on one side, with the employee/company details on the opposite side. We are looking for something that is very eye catching, modern, and bold.

Target Market(s)

This will target both drone pilots and drone businesses, along with all the industries that could utilize drone services (aerial video, aerial photos, inspections, 3d mapping, etc).

Industry/Entity Type

Business

```html
<!DOCTYPE html>
<html lang="en">
<head>
<meta charset="utf-8">
<title>Aerolift – Business Card</title>
<link rel="stylesheet" href="https://fonts.googleapis.com/css2?family=Montserrat:wght@400;500;600;700&display=swap">
<style>
  :root {
    --backdrop: #2b2b2b;
    --card: #050505;
    --teal: #2fc1cc;
    --white: #f4f4f4;
    --muted: #d8d8d8;
  }
  * { margin: 0; padding: 0; box-sizing: border-box; }
  html, body { width: 1200px; height: 900px; overflow: hidden; }
  body {
    background: var(--backdrop);
    font-family: "Montserrat", sans-serif;
    color: var(--white);
    position: relative;
  }
  .card {
    position: absolute;
    width: 560px;
    height: 320px;
    background: var(--card);
    border-radius: 26px;
    box-shadow: 0 18px 40px rgba(0,0,0,0.45);
    overflow: hidden;
  }
  .card--front { left: 140px; top: 100px; }
  .card--back { left: 500px; top: 480px; }

  .brand {
    position: absolute;
    left: 0; right: 0; top: 112px;
    text-align: center;
  }
  .brand__name {
    font-weight: 500;
    font-size: 40px;
    color: var(--white);
  }
  .front__web {
    position: absolute;
    left: 0; right: 0; bottom: 46px;
    text-align: center;
    font-size: 17px;
    font-weight: 500;
    color: var(--white);
  }
  .accent { color: var(--teal); font-weight: 600; }

  .back__band {
    position: absolute;
    left: 0; top: 150px;
    width: 34px; height: 140px;
    background: var(--teal);
    border-radius: 0 0 30px 0;
  }
  .details {
    position: absolute;
    left: 52px; top: 140px;
    line-height: 1.3;
  }
  .details__name {
    font-size: 26px;
    font-weight: 700;
    color: var(--teal);
  }
  .details__title {
    font-size: 15px;
    color: var(--muted);
    margin-bottom: 6px;
  }
  .details__line {
    font-size: 15px;
    color: var(--white);
    display: flex;
    align-items: center;
    gap: 8px;
  }
  .details__line svg { width: 13px; height: 13px; flex: none; }

  .back__mark {
    position: absolute;
    right: 40px; top: 60px;
    display: flex;
    align-items: center;
    gap: 12px;
  }
  .back__mark-dot {
    width: 18px; height: 18px;
    border-radius: 50%;
    background: var(--teal);
  }
  .back__mark-name {
    font-size: 24px;
    font-weight: 500;
    color: var(--white);
  }
</style>
</head>
<body>
  <section class="card card--front" aria-label="Card front">
    <div class="brand">
      <span class="brand__name">Aerolift</span>
    </div>
    <p class="front__web">www.<span class="accent">aerolift</span>.com</p>
  </section>

  <section class="card card--back" aria-label="Card back">
    <div class="back__band"></div>
    <div class="details">
      <p class="details__name">Marcus Hale</p>
      <p class="details__title">Director</p>
      <p class="details__line">48 Harbor Lane</p>
      <p class="details__line">Millbrook, NY 12000</p>
      <p class="details__line">
        <svg viewBox="0 0 16 16" aria-hidden="true"><path fill="#2fc1cc" d="M3 1l3 1 1 4-2 1c1 2 2 3 4 4l1-2 4 1 1 3-2 2C7 15 1 9 1 3z"/></svg>
        <span>+330 5510-2394</span>
      </p>
      <p class="details__line">
        <svg viewBox="0 0 16 16" aria-hidden="true"><rect x="1.5" y="3.5" width="13" height="9" rx="1" fill="none" stroke="#2fc1cc" stroke-width="1.6"/><path d="M2 4l6 5 6-5" fill="none" stroke="#2fc1cc" stroke-width="1.6"/></svg>
        <span>info@aerolift.com</span>
      </p>
      <p class="details__line">
        <svg viewBox="0 0 16 16" aria-hidden="true"><circle cx="8" cy="8" r="6.5" fill="none" stroke="#2fc1cc" stroke-width="1.5"/><path d="M1.5 8h13M8 1.5c-3 3.5-3 9.5 0 13M8 1.5c3 3.5 3 9.5 0 13" fill="none" stroke="#2fc1cc" stroke-width="1.2"/></svg>
        <span>www.<span class="accent">aerolift</span>.com</span>
      </p>
    </div>
    <div class="back__mark">
      <span class="back__mark-dot"></span>
      <span class="back__mark-name">Aerolift</span>
    </div>
  </section>
</body>
</html>
```